Quillmoor Farm Organic Flower Farm, Farmer Florist

I am a flower grower and florist, so I do everything from the field to the vase. I want to include my website, phone, email and instagram

```html
<!DOCTYPE html>
<html lang="en">
<head>
<meta charset="utf-8">
<title>Quillmoor Farm – Business Cards</title>
<link rel="stylesheet" href="https://fonts.googleapis.com/css2?family=Noto+Serif:wght@400&display=swap">
<style>
  :root {
    --backdrop: #8b8d8c;
    --maroon: #5e2d33;
    --blush: #f08c8c;
    --paper: #ffffff;
    --mist: #e6dadc;
  }
  * { box-sizing: border-box; margin: 0; padding: 0; }
  html, body {
    width: 1188px;
    height: 1200px;
    overflow: hidden;
    background: var(--backdrop);
    font-family: "Noto Serif", Georgia, serif;
  }
  .card {
    position: absolute;
    left: 245px;
    width: 696px;
    height: 386px;
    overflow: hidden;
  }
  .card--front { top: 159px; display: flex; }
  .card--back { top: 627px; background: var(--maroon); }

  .front__brand {
    width: 348px;
    height: 100%;
    background: var(--paper);
    position: relative;
  }
  .front__details {
    width: 348px;
    height: 100%;
    background: var(--maroon);
    padding: 100px 0 0 49px;
  }

  .brand {
    position: absolute;
    left: 0; right: 0;
    display: flex;
    flex-direction: column;
    align-items: center;
  }
  .brand__mark {
    background: var(--blush);
  }
  .brand__name {
    font-weight: 400;
    letter-spacing: 0.08em;
    line-height: 1;
    white-space: nowrap;
  }
  .front__brand .brand { top: 128px; }
  .front__brand .brand__mark { width: 26px; height: 26px; margin-bottom: 18px; }
  .front__brand .brand__name { font-size: 28px; color: var(--maroon); }

  .card--back .brand { top: 150px; }
  .card--back .brand__mark { width: 40px; height: 40px; margin-bottom: 26px; }
  .card--back .brand__name { font-size: 44px; color: var(--paper); }

  .person__name {
    font-size: 23px;
    color: var(--mist);
    line-height: 1.1;
    letter-spacing: 0.01em;
  }
  .person__role {
    font-size: 22px;
    color: var(--blush);
    line-height: 1.2;
  }
  .contacts {
    list-style: none;
    margin-top: 20px;
  }
  .contacts__item {
    display: flex;
    align-items: center;
    height: 28.5px;
    font-size: 20px;
    color: var(--mist);
    white-space: nowrap;
  }
  .contacts__icon {
    width: 20px;
    height: 20px;
    margin-right: 9px;
    flex: none;
    fill: var(--blush);
  }
  .contacts__badge {
    width: 18px;
    height: 18px;
    margin: 0 10px 0 1px;
    border-radius: 4px;
    background: var(--blush);
    flex: none;
  }
</style>
</head>
<body>
  <section class="card card--front">
    <div class="front__brand">
      <div class="brand">
        <span class="brand__mark"></span>
        <span class="brand__name">QUILLMOOR</span>
      </div>
    </div>
    <div class="front__details">
      <p class="person__name">DANIEL HARTLEY</p>
      <p class="person__role">Owner</p>
      <ul class="contacts">
        <li class="contacts__item">
          <svg class="contacts__icon" viewBox="0 0 20 20" aria-hidden="true">
            <path d="M2 6c0-2 3-3 8-3s8 1 8 3v2h-4V6.5c-1-.5-2.5-.7-4-.7s-3 .2-4 .7V8H2z"/>
            <path d="M5 9h10l2 8H3z"/>
          </svg>
          <span>+56912407731</span>
        </li>
        <li class="contacts__item">
          <svg class="contacts__icon" viewBox="0 0 20 20" aria-hidden="true">
            <path d="M1 4h18v12H1z M2.5 5.5 10 11l7.5-5.5" fill="var(--blush)" stroke="var(--maroon)" stroke-width="1.2"/>
          </svg>
          <span>info@quillmoor.com</span>
        </li>
        <li class="contacts__item">
          <svg class="contacts__icon" viewBox="0 0 20 20" aria-hidden="true">
            <circle cx="10" cy="10" r="9.5"/>
            <path d="M5 5c2 0 3 1 3 3s-2 2-2 4-2 1-3-1 0-6 2-6zm7 6c2 0 3 1 2 3s-3 3-4 1 0-4 2-4zm0-8c2 1 3 2 2 3s-3 0-3-1 0-2 1-2z" fill="var(--maroon)"/>
          </svg>
          <span>www.quillmoor.com</span>
        </li>
        <li class="contacts__item">
          <span class="contacts__badge"></span>
          <span>@quillmoor</span>
        </li>
      </ul>
    </div>
  </section>

  <section class="card card--back">
    <div class="brand">
      <span class="brand__mark"></span>
      <span class="brand__name">QUILLMOOR</span>
    </div>
  </section>
</body>
</html>
```